Corvix Thinner Logo and Packaging Design

We are seeking a striking and professional logo and packaging design for our new product line, Corvix Thinner. This logo will be used on the packaging for three different sizes of half-transparent carboys: 1L, 4L, and 20L. Corvix Thinner is a high-quality solvent brand known for its excellent solvency, fast-drying properties, and pleasant smell. The logo should feature an eagle motif to symbolize power and precision, and our slogan, "FLY WITH QUALITY." The design should be suitable for placement on hardware store and warehouse shelves. Additionally, we need the designer to create an eagle logo to accompany the packaging.

Packaging Dimensions:
1L Carboy:
Front: 71mm height x 142mm width
Side: 71mm height x 73mm width
4L Carboy:
Front: 160mm height x 170mm width
Side: 160mm height x 120mm width
20L Carboy:
Front: 245mm height x 190mm width
Side: 215mm height x 190mm width
Front Label Requirements:

Product Name: Thinner QZR
Volume: 20L
Precautionary Statements:
Keep Away from Sources of ignition - No Smoking
Avoid Contact with Eyes
Do Not Empty into Drains or Sewers
Take Precautionary Measures Against Static Discharge
Hazard Statements:
Flammable Liquid and Vapor
May be fatal if swallowed or enters Airways
Causes Skin Irritation
Causes Serious Eye Irritation
Causes Damage to Organs if Prolonged or Repeated Exposure
Hazard Pictograms: (Include relevant hazard symbols)
Design Requirements:

Logo: Eagle motif (to be designed by the designer)
Slogan: FLY WITH QUALITY
Color Scheme: Designer to recommend (should be striking and professional for retail display)

Please see my latest picture. Kindly note the packaging is in Plastic Carboy (not in metal tin as per PS).

Eagle to be more majestic and bigger (as if soaring in the sky).
Singapore landscape as background to have Singapore identity such as KDT, Lumen Loop, terraces of mistral etc.

Eagle to be more majestic and bigger, wings to spread wide.
We not want it to be of photo style, but more on a cartoon style. Please see my latest file uploaded.

Target Market(s)

Our target market includes painting companies, construction companies, direct household consumers, and industrial users who require high-quality solvents for various applications.

Industry/Entity Type

Chemical, spray paint and painting, household, industrial

Requirements
Must have
• Professional and Striking Design: Eye-catching and professional packaging for retail shelves. Eagle Logo: A strong, precise eagle logo. Slogan: "FLY WITH QUALITY" prominently displayed. Clear Precautionary and Hazard Statements: Important safety information and pictograms. Volume Indication: Clearly marked (e.g., 1L, 4L, 20L). Eagle to be more majestic and bigger (as if soaring in the sky). Singapore landscape as background to have Singapore identity such as KDT, Lumen Loop, terraces of mistral etc.
Nice to have
• Color Scheme Recommendations: Suggestions for a professional, striking color scheme. Versatility: Design elements adaptable across different sizes of packaging. Environmentally Friendly Elements: Indications of sustainability or eco-friendliness in the design.
Should not have
• Overly Complex Designs: Avoid cluttered or overly intricate designs that detract from readability. Inconsistent Branding: Ensure all elements are cohesive and align with the brand identity.

```html
<!DOCTYPE html>
<html lang="en">
<head>
<meta charset="utf-8">
<title>Corvix Thinner – Thinner QZR 20L Label</title>
<link rel="stylesheet" href="https://fonts.googleapis.com/css2?family=Montserrat:wght@500;600;700;800;900&display=swap">
<style>
  :root {
    --backdrop: #e4e4e4;
    --label-white: #f4f4f4;
    --brand-orange: #dd5a31;
    --brand-orange-deep: #d24f2a;
    --ink-dark: #3a3a3a;
    --text-light: #ffffff;
    --warning-yellow: #f2b418;
    --warning-ink: #2a2a2a;
  }
  * { box-sizing: border-box; margin: 0; padding: 0; }
  html, body {
    width: 1200px;
    height: 722px;
    overflow: hidden;
    background: var(--backdrop);
    font-family: "Montserrat", Arial, sans-serif;
  }
  .canvas {
    position: relative;
    width: 1200px;
    height: 722px;
  }
  .packaging {
    position: absolute;
    left: 230px;
    top: 80px;
    display: flex;
    height: 560px;
  }
  .panel {
    position: relative;
    height: 100%;
    background: var(--label-white);
    overflow: hidden;
  }
  .panel-side { width: 300px; border-right: 1px solid #dadada; }
  .panel-front { width: 440px; }

  .product-band {
    position: absolute;
    top: 0;
    left: 0;
    width: 100%;
    height: 62px;
    background: var(--brand-orange);
    color: var(--text-light);
    font-weight: 700;
    letter-spacing: 1px;
    display: flex;
    align-items: center;
    justify-content: center;
  }
  .panel-side .product-band { font-size: 18px; }
  .panel-front .product-band { font-size: 24px; }

  .lower-panel {
    position: absolute;
    top: 300px;
    left: 0;
    width: 100%;
    height: 260px;
    background: linear-gradient(180deg, var(--brand-orange-deep), var(--brand-orange));
  }

  .brand-lockup {
    position: absolute;
    left: 0;
    width: 100%;
    display: flex;
    flex-direction: column;
    align-items: center;
  }
  .brand-mark { background: var(--brand-orange); }
  .brand-name {
    font-weight: 600;
    color: var(--ink-dark);
    text-transform: uppercase;
    letter-spacing: 1.5px;
  }
  .panel-side .brand-lockup { top: 112px; gap: 16px; }
  .panel-side .brand-mark { width: 44px; height: 44px; }
  .panel-side .brand-name { font-size: 17px; }
  .panel-front .brand-lockup { top: 108px; gap: 18px; }
  .panel-front .brand-mark { width: 60px; height: 60px; }
  .panel-front .brand-name { font-size: 25px; }

  .slogan {
    position: absolute;
    left: 0;
    width: 100%;
    font-weight: 900;
  }
  .slogan-top { display: block; color: var(--brand-orange); }
  .slogan-bottom { display: block; color: var(--text-light); }
  .panel-side .slogan {
    top: 250px;
    padding-left: 18px;
    font-size: 44px;
    line-height: 46px;
  }
  .panel-front .slogan {
    top: 232px;
    text-align: center;
    font-size: 66px;
    line-height: 66px;
  }

  .safety-info {
    position: absolute;
    left: 24px;
    top: 392px;
    width: 240px;
    color: var(--text-light);
  }
  .safety-heading { font-weight: 700; font-size: 9px; margin-bottom: 3px; }
  .safety-list {
    list-style: none;
    font-weight: 500;
    font-size: 7px;
    line-height: 10px;
    margin-bottom: 10px;
  }
  .safety-list li::before { content: "• "; }

  .volume {
    position: absolute;
    right: 34px;
    top: 378px;
    color: var(--text-light);
    font-weight: 700;
    font-size: 54px;
    letter-spacing: 1px;
  }
  .pictograms {
    position: absolute;
    right: 34px;
    top: 456px;
    display: flex;
    gap: 8px;
  }
  .pictograms svg { width: 28px; height: 26px; display: block; }
</style>
</head>
<body>
<main class="canvas">
  <div class="packaging">
    <section class="panel panel-side" aria-label="Side label">
      <header class="product-band">THINNER QZR</header>
      <div class="lower-panel"></div>
      <div class="brand-lockup">
        <span class="brand-mark" aria-hidden="true"></span>
        <span class="brand-name">Corvix Thinner</span>
      </div>
      <p class="slogan">
        <span class="slogan-top">FLY WITH</span>
        <span class="slogan-bottom">QUALITY</span>
      </p>
    </section>

    <section class="panel panel-front" aria-label="Front label">
      <header class="product-band">THINNER QZR</header>
      <div class="lower-panel"></div>
      <div class="brand-lockup">
        <span class="brand-mark" aria-hidden="true"></span>
        <span class="brand-name">Corvix Thinner</span>
      </div>
      <h1 class="slogan">
        <span class="slogan-top">FLY WITH</span>
        <span class="slogan-bottom">QUALITY</span>
      </h1>

      <div class="safety-info">
        <h2 class="safety-heading">Precautionary</h2>
        <ul class="safety-list">
          <li>Keep Away from Sources of Ignition - No Smoking</li>
          <li>Avoid Contact with Eyes</li>
          <li>Do Not Empty into Drains or Sewers</li>
          <li>Take Precautionary Measures Against Static Discharge</li>
        </ul>
        <h2 class="safety-heading">Hazard</h2>
        <ul class="safety-list">
          <li>Flammable Liquid and Vapor</li>
          <li>May be fatal if swallowed or enters Airways</li>
          <li>Causes Skin Irritation</li>
          <li>Causes Serious Eye Irritation</li>
          <li>Causes Damage to Organs if Prolonged or Repeated Exposure</li>
        </ul>
      </div>

      <div class="volume">20L</div>

      <div class="pictograms" aria-label="Hazard warnings">
        <svg viewBox="0 0 28 26" role="img" aria-label="Warning">
          <polygon points="14,2 27,24 1,24" fill="var(--warning-yellow)" stroke="var(--warning-ink)" stroke-width="1.5" stroke-linejoin="round"/>
          <rect x="12.8" y="9" width="2.4" height="8" fill="var(--warning-ink)"/>
          <rect x="12.8" y="19" width="2.4" height="2.4" fill="var(--warning-ink)"/>
        </svg>
        <svg viewBox="0 0 28 26" role="img" aria-label="Warning">
          <polygon points="14,2 27,24 1,24" fill="var(--warning-yellow)" stroke="var(--warning-ink)" stroke-width="1.5" stroke-linejoin="round"/>
          <rect x="12.8" y="9" width="2.4" height="8" fill="var(--warning-ink)"/>
          <rect x="12.8" y="19" width="2.4" height="2.4" fill="var(--warning-ink)"/>
        </svg>
        <svg viewBox="0 0 28 26" role="img" aria-label="Warning">
          <polygon points="14,2 27,24 1,24" fill="var(--warning-yellow)" stroke="var(--warning-ink)" stroke-width="1.5" stroke-linejoin="round"/>
          <rect x="12.8" y="9" width="2.4" height="8" fill="var(--warning-ink)"/>
          <rect x="12.8" y="19" width="2.4" height="2.4" fill="var(--warning-ink)"/>
        </svg>
      </div>
    </section>
  </div>
</main>
</body>
</html>
```